Marrowfield Dental
Professional
Dr. Lien Vu
Marrowfield Dental - (Business name)
418-265 West Harlow St.
Vancouver, BC
V6R 2K8
info@coastal-smilecare-bc.ca
www.coastal-smilecare-bc.ca
Logo of Marrowfield Dental
Name, address, phone #.... smaller in corner maybe? Use logo designed.
Your next appointment:_________________
at _______am/pm.
See you soon!
(something like that)
Vector logo
Vector logo (wide)

```html
<!DOCTYPE html>
<html lang="en">
<head>
<meta charset="utf-8">
<title>Marrowfield Dental – Business Card</title>
<link rel="stylesheet" href="https://fonts.googleapis.com/css2?family=Arimo:wght@400;700&family=Nunito:wght@800&family=PT+Serif&display=swap">
<style>
  :root {
    --stage: #a9a9a9;
    --paper: #ffffff;
    --blue-light: #5d8fe2;
    --blue-mid: #3563c4;
    --blue-deep: #1b2e74;
    --navy: #1e295b;
    --navy-dark: #161f49;
    --gold: #f2c318;
    --ink: #1c1c1c;
    --line: #2a3a7a;
  }
  * { box-sizing: border-box; margin: 0; padding: 0; }
  html, body { width: 1200px; height: 933px; overflow: hidden; }
  body { background: var(--stage); position: relative; font-family: "Arimo", Arial, sans-serif; }

  .card {
    position: absolute;
    width: 731px;
    height: 431px;
    background: var(--paper);
    border: 1px solid var(--line);
    overflow: hidden;
  }
  .card--front { left: 25px; top: 30px; }
  .card--back  { left: 444px; top: 462px; }

  .card__shape { position: absolute; inset: 0; width: 100%; height: 100%; }

  .brand {
    position: absolute;
    font-family: "Nunito", Arial, sans-serif;
    font-weight: 800;
    white-space: nowrap;
  }
  .card--front .brand { left: 54px; top: 46px; font-size: 36px; color: var(--paper); letter-spacing: 0.5px; }
  .card--back .brand  { left: 36px; top: 344px; font-size: 22px; color: var(--blue-deep); }

  .doctor {
    position: absolute;
    left: 58px; top: 205px;
    font-family: "PT Serif", Georgia, serif;
    font-size: 31px;
    color: var(--paper);
  }

  .contact {
    position: absolute;
    right: 26px; top: 228px;
    font-size: 17px;
    line-height: 24.5px;
    color: var(--ink);
    text-align: right;
  }
  .contact__address { margin-bottom: 35px; }
  .contact__row { display: flex; justify-content: flex-end; gap: 10px; }

  .appointment {
    position: absolute;
    left: 186px; top: 114px;
    color: var(--paper);
    font-weight: 700;
    font-size: 19px;
  }
  .appointment__line { margin-bottom: 20px; }
  .appointment__blank {
    display: inline-block;
    border-bottom: 2px dotted var(--paper);
    vertical-align: baseline;
  }
  .appointment__date { width: 374px; height: 22px; margin-bottom: 22px; }
  .appointment__time { width: 120px; height: 16px; margin: 0 6px; }

  .farewell {
    position: absolute;
    right: 28px; top: 296px;
    color: var(--paper);
    font-weight: 700;
    font-size: 20px;
  }
</style>
</head>
<body>

<section class="card card--front" aria-label="Business card front">
  <svg class="card__shape" viewBox="0 0 731 431" preserveAspectRatio="none" aria-hidden="true">
    <defs>
      <linearGradient id="front-panel" x1="0" y1="0" x2="1" y2="0.4">
        <stop offset="0" stop-color="var(--blue-light)"/>
        <stop offset="0.55" stop-color="var(--blue-mid)"/>
        <stop offset="1" stop-color="var(--blue-deep)"/>
      </linearGradient>
    </defs>
    <path d="M0 0 H440 C505 45 520 130 462 222 C412 300 382 360 372 431 H0 Z" fill="url(#front-panel)"/>
    <path d="M440 0 C505 45 520 130 462 222 C412 300 382 360 372 431" fill="none" stroke="var(--blue-deep)" stroke-width="7"/>
    <path d="M452 0 C518 46 532 132 474 224 C424 302 394 360 384 431" fill="none" stroke="var(--gold)" stroke-width="3"/>
  </svg>

  <div class="brand">Marrowfield Dental</div>
  <div class="doctor">Dr. Lien Vu</div>

  <div class="contact">
    <div class="contact__address">
      <div>418-265 West Harlow St.</div>
      <div>Vancouver, BC, V6R 2K8</div>
    </div>
    <div class="contact__row"><span>Phone</span><span>604-555-0142</span></div>
    <div class="contact__row"><span>Fax</span><span>604-555-0143</span></div>
    <div class="contact__row"><span>Email</span><span>info@coastal-smilecare-bc.ca</span></div>
    <div class="contact__row"><span>Web</span><span>www.coastal-smilecare-bc.ca</span></div>
  </div>
</section>

<section class="card card--back" aria-label="Appointment card back">
  <svg class="card__shape" viewBox="0 0 731 431" preserveAspectRatio="none" aria-hidden="true">
    <defs>
      <linearGradient id="back-panel" x1="0" y1="0" x2="1" y2="1">
        <stop offset="0" stop-color="var(--navy)"/>
        <stop offset="1" stop-color="var(--navy-dark)"/>
      </linearGradient>
    </defs>
    <rect width="731" height="431" fill="url(#back-panel)"/>
    <path d="M0 0 H150 C100 90 20 180 60 250 C90 300 330 300 420 431 H0 Z" fill="var(--paper)"/>
    <path d="M150 0 C100 90 20 180 60 250 C90 300 330 300 420 431" fill="none" stroke="var(--blue-deep)" stroke-width="6"/>
    <path d="M140 0 C90 90 10 180 50 252 C80 304 315 306 402 431" fill="none" stroke="var(--gold)" stroke-width="3"/>
  </svg>

  <div class="appointment">
    <div class="appointment__line">Your next appointment:</div>
    <div><span class="appointment__blank appointment__date"></span></div>
    <div>at<span class="appointment__blank appointment__time"></span>am/pm.</div>
  </div>

  <div class="farewell">See you soon!</div>
  <div class="brand">Marrowfield Dental</div>
</section>

</body>
</html>
```